Business Card Design

I am starting my therapy private practice. I will be an in home therapist, so I go into family's homes instead of using an office to do family/marriage therapy. Therefore, I do not have an office address. I am looking for something in the black, red, gray, and blue color scheme that appeals to both families, couples and teenagers.

Industry/Entity Type

Business

Contact Information for Business Card

Lena Brightwell, MS, MFT Intern
Marriage and Family Therapy
In Home Therapist
617-482-5190
Lena@LenaBrightwell-example.com

```html
<!DOCTYPE html>
<html lang="en">
<head>
<meta charset="utf-8">
<title>Lena Brightwell – Business Card</title>
<link rel="stylesheet" href="https://fonts.googleapis.com/css2?family=Tinos:ital,wght@0,700;1,700&display=swap">
<style>
  :root {
    --page: #ffffff;
    --card-blue: #00adee;
    --band-black: #231f20;
    --ink-white: #ffffff;
  }
  * { margin: 0; padding: 0; box-sizing: border-box; }
  html, body {
    width: 1200px;
    height: 1000px;
    overflow: hidden;
    background: var(--page);
  }
  .canvas {
    position: relative;
    width: 1200px;
    height: 1000px;
    background: var(--page);
  }
  .card {
    position: absolute;
    left: 120px;
    top: 203px;
    width: 977px;
    height: 590px;
    background: var(--card-blue);
  }
  .name-band {
    position: absolute;
    left: 0;
    top: 156px;
    width: 977px;
    height: 111px;
    background: var(--band-black);
  }
  .name {
    position: absolute;
    left: 32px;
    top: 142px;
    font-family: "Tinos", "Times New Roman", serif;
    font-style: italic;
    font-weight: 700;
    font-size: 104px;
    line-height: 1;
    color: var(--ink-white);
    white-space: nowrap;
    letter-spacing: 1px;
  }
  .credentials {
    position: absolute;
    left: 32px;
    top: 278px;
    font-family: "Tinos", "Times New Roman", serif;
    font-weight: 700;
    font-size: 19.5px;
    line-height: 1;
    color: var(--ink-white);
    white-space: nowrap;
  }
  .contact-box {
    position: absolute;
    left: 537px;
    top: 491px;
    width: 440px;
    height: 99px;
    background: var(--band-black);
  }
  .contact-list {
    position: absolute;
    left: 46px;
    top: 20px;
    list-style: none;
    font-family: "Tinos", "Times New Roman", serif;
    font-weight: 700;
    font-size: 22px;
    line-height: 30px;
    color: var(--ink-white);
    white-space: nowrap;
  }
  .contact-item {
    display: flex;
    align-items: center;
    gap: 8px;
  }
  .contact-icon {
    width: 18px;
    height: 18px;
    flex: none;
    display: inline-flex;
    align-items: center;
    justify-content: center;
    fill: var(--ink-white);
    font-size: 21px;
  }
</style>
</head>
<body>
  <main class="canvas">
    <section class="card" aria-label="Business card for Lena Brightwell">
      <div class="name-band"></div>
      <h1 class="name">Lena Brightwell</h1>
      <p class="credentials">MS, MFT Intern Marriage and Family Therapy In Home Therapist</p>
      <div class="contact-box">
        <ul class="contact-list">
          <li class="contact-item">
            <svg class="contact-icon" viewBox="0 0 24 24" aria-hidden="true">
              <path d="M6.6 2.5c.6-.3 1.3-.1 1.6.5l2 3.8c.3.6.1 1.2-.4 1.6l-1.6 1.1c.9 2.1 2.4 3.9 4.3 5.1l1.3-1.4c.4-.5 1.1-.6 1.6-.2l3.5 2.4c.5.4.7 1.1.3 1.7l-1.3 2.2c-.5.8-1.5 1.2-2.4.9C9.9 18.5 5.1 12.5 4.3 6.2c-.1-.9.3-1.8 1.1-2.3z"/>
            </svg>
            <span class="contact-phone">617-482-5190</span>
          </li>
          <li class="contact-item">
            <span class="contact-icon" aria-hidden="true">@</span>
            <span class="contact-email">lena@lenabrightwell-example.com</span>
          </li>
        </ul>
      </div>
    </section>
  </main>
</body>
</html>
```